KayVrix - The Hour of Ninety Suns Mixtape Cover

I need a cover for my first mixtape titled "The Hour of Ninety Suns". The mixtape is very energetic and original with a unique approach to it's message. I want the cover to capture the listeners eye as much as the music. I'm open to seeing different types of designs. I would like my name "KayVrix" to be on the front as well as the title. I've uploaded three pictures that the designer can choose from.

Target Market(s)

Hip-Hop Community

Font styles to use
Sans Serif

Requirements
Must have
• My picture, my name, the title of the project (The Hour of Ninety Suns)
Nice to have
• background graphics

```html
<!DOCTYPE html>
<html lang="en">
<head>
<meta charset="utf-8">
<title>KayVrix – The Hour of Ninety Suns</title>
<link href="https://fonts.googleapis.com/css2?family=Graduate&display=swap" rel="stylesheet">
<style>
  :root {
    --stage: #2f2f33;
    --cover-black: #0b0c10;
    --ink-light: #f1efe9;
    --tone-red: #b8283a;
    --tone-deep-red: #7a1a26;
    --tone-blue: #2b4f8f;
    --tone-navy: #1a2545;
    --tone-cyan: #4fb3c9;
    --tone-yellow: #c9b24a;
    --tone-skin: #8a5a48;
    --tone-white: #dcd8d0;
  }
  * { margin: 0; padding: 0; box-sizing: border-box; }
  html, body {
    width: 1200px;
    height: 668px;
    overflow: hidden;
    background: var(--stage);
  }
  .stage {
    width: 1200px;
    height: 668px;
    display: flex;
    align-items: center;
    justify-content: center;
  }
  .cover {
    position: relative;
    width: 610px;
    height: 610px;
    background: var(--cover-black);
    overflow: hidden;
  }
  .cover__portrait {
    position: absolute;
    top: 0;
    right: 0;
    width: 430px;
    height: 610px;
    background:
      linear-gradient(180deg,
        var(--tone-white) 0%,
        var(--tone-red) 14%,
        var(--tone-skin) 28%,
        #3a2a2c 44%,
        var(--tone-yellow) 56%,
        var(--tone-red) 68%,
        var(--tone-navy) 82%,
        var(--tone-deep-red) 100%);
    -webkit-mask-image: linear-gradient(90deg, transparent 0%, rgba(0,0,0,0.85) 28%, #000 55%, rgba(0,0,0,0.9) 100%);
            mask-image: linear-gradient(90deg, transparent 0%, rgba(0,0,0,0.85) 28%, #000 55%, rgba(0,0,0,0.9) 100%);
    opacity: 0.9;
  }
  .cover__title {
    position: absolute;
    left: 24px;
    top: 252px;
    font-family: "Graduate", serif;
    font-weight: 400;
    font-size: 38px;
    line-height: 1;
    letter-spacing: 1px;
    color: var(--ink-light);
    text-transform: uppercase;
    white-space: nowrap;
    text-shadow: 0 1px 3px rgba(0,0,0,0.6);
  }
  .cover__artist {
    position: absolute;
    right: 22px;
    bottom: 18px;
    font-family: "Graduate", serif;
    font-size: 17px;
    line-height: 1;
    letter-spacing: 1.5px;
    color: var(--ink-light);
    text-transform: uppercase;
  }
</style>
</head>
<body>
  <main class="stage">
    <section class="cover">
      <div class="cover__portrait" role="img" aria-label="Painterly portrait of the artist in profile wearing a patterned bandana, hands pressed together in prayer, streaked with red, blue, yellow and white brush strokes on black"></div>
      <h1 class="cover__title">The Hour of Ninety Suns</h1>
      <p class="cover__artist">KayVrix</p>
    </section>
  </main>
</body>
</html>
```